Business Card Design for Irrigation Contractor

Design and layout for company business cards to include the following information:
1. Logo
2. Installation \ Service \ Maintenance
3. U-47326
4. Walter K. Lindqvist
5. walter@kelvaspray.com
6. Office 561-738-2196
7. Cell 561-629-8513

```html
<!DOCTYPE html>
<html lang="en">
<head>
<meta charset="utf-8">
<title>Kelva Spray — Business Card</title>
<link rel="stylesheet" href="https://fonts.googleapis.com/css2?family=Montserrat:wght@400;500;700;800&display=swap">
<style>
  :root {
    --backdrop: #1b1b1d;
    --navy: #0b3a6b;
    --navy-deep: #072a4f;
    --blue: #1569b3;
    --blue-bright: #1a74c2;
    --paper: #ffffff;
    --ink: #2a2f38;
    --rule: #8a8f96;
  }
  * { margin: 0; padding: 0; box-sizing: border-box; }
  html, body {
    width: 1200px; height: 895px; overflow: hidden;
    background: var(--backdrop);
    font-family: "Montserrat", Arial, sans-serif;
  }
  .canvas { position: relative; width: 1200px; height: 895px; }

  .card {
    position: absolute; width: 620px; height: 354px; overflow: hidden;
    box-shadow: 0 18px 40px rgba(0,0,0,.55);
  }

  /* Front */
  .card-front {
    left: 70px; top: 70px;
    background: radial-gradient(ellipse at 48% 40%, var(--blue-bright) 0%, var(--navy) 55%, var(--navy-deep) 100%);
    color: var(--paper);
    display: flex; flex-direction: column; align-items: center; justify-content: center;
  }
  .brand { display: flex; align-items: center; gap: 14px; }
  .brand-dot { width: 34px; height: 34px; border-radius: 50%; background: currentColor; }
  .brand-name { font-weight: 800; font-size: 44px; letter-spacing: 1px; line-height: 1; }
  .tagline { margin-top: 14px; font-weight: 500; font-size: 17px; letter-spacing: 1.4px; }

  /* Back */
  .card-back { left: 510px; top: 470px; background: var(--paper); color: var(--ink); }
  .back-brand { position: absolute; left: 46px; top: 58px; color: var(--navy); }
  .back-brand .brand-dot { width: 26px; height: 26px; }
  .back-brand .brand-name { font-size: 30px; }

  .divider { position: absolute; left: 46px; top: 170px; width: 340px; height: 1px; background: var(--rule); }

  .holder { position: absolute; right: 40px; top: 130px; text-align: right; }
  .holder-name { font-weight: 800; font-size: 22px; color: var(--blue); text-transform: uppercase; letter-spacing: .3px; }
  .holder-address { margin-top: 12px; font-size: 13px; line-height: 1.45; color: var(--ink); }

  .contacts { position: absolute; left: 56px; top: 186px; list-style: none; font-size: 15px; line-height: 1; }
  .contacts li { display: flex; align-items: center; gap: 10px; height: 23px; }
  .contacts svg { width: 13px; height: 13px; fill: var(--blue); flex: none; }

  .footer-band { position: absolute; left: 0; right: 0; bottom: 0; height: 22px; background: var(--navy); }
  .license-tab {
    position: absolute; right: 48px; bottom: 0; width: 140px; height: 62px;
    background: var(--blue); color: var(--paper);
    clip-path: polygon(10% 0, 100% 0, 92% 100%, 0 100%);
    display: flex; align-items: center; justify-content: center;
    font-weight: 800; font-size: 19px; letter-spacing: .5px;
  }
  .license-edge {
    position: absolute; right: 190px; bottom: 0; width: 22px; height: 34px;
    background: var(--navy); clip-path: polygon(35% 0, 100% 0, 65% 100%, 0 100%);
  }
</style>
</head>
<body>
<main class="canvas">
  <section class="card card-front">
    <div class="brand">
      <span class="brand-dot"></span>
      <span class="brand-name">KELVA SPRAY</span>
    </div>
    <p class="tagline">Installation | Service | Maintenance</p>
  </section>

  <section class="card card-back">
    <div class="brand back-brand">
      <span class="brand-dot"></span>
      <span class="brand-name">KELVA SPRAY</span>
    </div>

    <div class="divider"></div>

    <div class="holder">
      <h1 class="holder-name">Walter K. Lindqvist</h1>
      <p class="holder-address">48 Harbor Tower, Street# B<br>Dhaka, Bangladesh 1216</p>
    </div>

    <ul class="contacts">
      <li><svg viewBox="0 0 16 16"><path d="M3 1l3 3-2 2c1 2 3 4 5 5l2-2 3 3-2 3C6 15 1 10 1 3z"/></svg>561-629-8513</li>
      <li><svg viewBox="0 0 16 16"><path d="M1 6c0-2 3-4 7-4s7 2 7 4l-3 1-1-2H5L4 7zM3 8h10l1 6H2z"/></svg>561-738-2196</li>
      <li><svg viewBox="0 0 16 16"><path d="M1 3h14v10H1zM2 4l6 5 6-5"/></svg>walter@kelvaspray.com</li>
      <li><svg viewBox="0 0 16 16"><path d="M8 1a7 7 0 1 0 0 14A7 7 0 0 0 8 1zm0 1.5c1 1 1.6 3 1.7 4.7H6.3C6.4 5.5 7 3.5 8 2.5zM2.6 7.2a5.5 5.5 0 0 1 2.6-4 8 8 0 0 0-.9 4zm0 1.6h1.7c0 1.5.4 2.9.9 4a5.5 5.5 0 0 1-2.6-4zm3.7 0h3.4C9.6 10.5 9 12.5 8 13.5c-1-1-1.6-3-1.7-4.7zm5.4 0h1.7a5.5 5.5 0 0 1-2.6 4c.5-1.1.9-2.5.9-4zm0-1.6a8 8 0 0 0-.9-4 5.5 5.5 0 0 1 2.6 4z"/></svg>kelvaspray.com</li>
    </ul>

    <div class="footer-band"></div>
    <div class="license-edge"></div>
    <div class="license-tab">U-47326</div>
  </section>
</main>
</body>
</html>
```